International Used Food Processing Equipment company needs an awesome website!

We have been in business now for more than 15 years, and we are now launching a new website where international and USA based customers can view photos, descriptions, and ask questions of industrial food processing equipment.

We want the site to be vibrant and but yet communicate a professional tone to our customers. Most of our customers are older males, and the site must be easy to navigate, with easy on the eye color scheme. We want to features a lot of photos and a excellent equipment descriptions, with links where visitors can click on an item to send us a request for more information. We require easy to read font, clear navigation buttons and clear contact information to be found on each page.

Some of our competitors sites:
www.QRTDeals.example
www.caldrovenworks.example
www.plovetcorp.example

Our business name and logo is attached, but this is a rending of an image that was made about 10 years ago. Please let us know if you have any questions.

Target Market(s)

Food processing companies (canneries, fresh cut sector, large catering companies) in the USA and South America.

Logo Text

Excellent Machines at Excellent Prices

Coding

Coded - Design and coding required

Number of Pages Required

5+ page

Colors

Designer to choose colors to be used in the design.

Requirements
Must have
• Easy to navigate photo galleries, easy category search and easy machine search by keywords.
• Event Calendar
• Sign-up page for email newsletter
Nice to have
• Blog feature or latest news
• Past projects page
Should not have
• Hard to read font

```html
<!DOCTYPE html>
<html lang="en">
<head>
<meta charset="utf-8">
<title>Kettleworth Supply — Used Food Processing Equipment</title>
<link rel="stylesheet" href="https://fonts.googleapis.com/css2?family=Poppins:wght@400;500;600;700&family=Open+Sans:wght@400;600;700&display=swap">
<style>
:root{
  --orange:#f26522;
  --ink:#111111;
  --text:#444444;
  --light:#f4f1f1;
  --steel-hi:#dfe3e7;
  --steel-mid:#9aa3ab;
  --steel-lo:#4f575e;
  --white:#ffffff;
}
*{box-sizing:border-box;margin:0;padding:0}
html,body{width:1200px;height:4651px;overflow:hidden}
body{font-family:'Open Sans',sans-serif;color:var(--text);background:var(--white);position:relative}
h1,h2,h3,h4,h5,.nav,.btn{font-family:'Poppins',sans-serif}
.abs{position:absolute}
.photo{background:radial-gradient(ellipse at 35% 30%,var(--steel-hi),var(--steel-mid) 55%,var(--steel-lo))}
.btn{display:inline-flex;align-items:center;justify-content:center;background:var(--orange);color:var(--white);font-weight:600;font-size:13px;text-transform:uppercase;letter-spacing:.5px}
.section-title{position:absolute;left:0;width:1200px;text-align:center;font-size:30px;font-weight:700;color:var(--ink);text-transform:uppercase}
.section-title::after{content:"";display:block;width:36px;height:2px;background:#999;margin:16px auto 0}

/* header */
.site-header{top:0;left:0;width:1200px;height:136px;background:var(--white)}
.brand{left:110px;top:12px;display:flex;align-items:center;gap:12px}
.brand-mark{width:62px;height:118px;background:linear-gradient(#3a3a3a,#111)}
.brand-name{font-family:'Poppins',sans-serif;font-weight:700;font-size:22px;color:var(--ink);line-height:1.1;margin-top:-40px}
.brand-name small{display:block;font-size:13px;font-weight:600}
.follow{left:642px;top:38px;display:flex;align-items:center;gap:6px;font-size:11px;font-weight:600;color:var(--ink)}
.dot{width:24px;height:24px;border-radius:50%;background:#1d63b8}
.call{left:858px;top:30px;display:flex;align-items:center;gap:12px}
.call-icon{width:32px;height:32px;border-radius:50%;background:#333;display:flex;align-items:center;justify-content:center}
.call-text{font-size:11px;font-weight:700;color:var(--ink)}
.call-text b{display:block;font-family:'Poppins',sans-serif;font-size:24px;color:var(--orange);line-height:1.1}
.nav{left:582px;top:94px;display:flex;gap:30px;font-size:14px;font-weight:600;color:var(--ink);list-style:none}
.nav li:first-child{color:var(--orange)}

/* hero */
.hero{top:136px;left:0;width:1200px;height:552px;background:radial-gradient(ellipse at 45% 35%,#c4cacf,#8a9299 50%,#4e555b)}
.hero h1{position:absolute;top:196px;width:1200px;text-align:center;color:var(--white);font-size:40px;font-weight:700}
.search{position:absolute;top:280px;left:288px;display:flex;gap:19px}
.field{height:42px;background:var(--white);font-size:13px;color:#555;display:flex;align-items:center;padding:0 16px;justify-content:space-between;text-transform:uppercase}
.search .btn{width:152px;height:42px;font-size:16px}
.dots{position:absolute;top:502px;left:550px;display:flex;gap:10px}
.dots i{width:8px;height:8px;border-radius:50%;background:rgba(255,255,255,.7)}
.dots i:nth-child(3){background:var(--white);transform:scale(1.4)}

/* projects */
.project{position:absolute;top:855px;width:236px}
.project .photo{height:270px;background:radial-gradient(ellipse at 50% 45%,#c4c9ce,#eef0f2 70%,#ffffff)}
.project-label{margin:36px auto 0;width:136px;height:32px;background:#eeeeee;font-family:'Poppins',sans-serif;font-size:13px;font-weight:600;color:#333;display:flex;align-items:center;justify-content:center;box-shadow:0 2px 4px rgba(0,0,0,.15)}
.arrow{position:absolute;top:996px;width:32px;height:36px;background:#333;display:flex;align-items:center;justify-content:center}

/* welcome */
.welcome{top:1265px;left:0;width:1200px;height:459px;background:var(--light)}
.welcome .photo{position:absolute;left:0;top:0;width:580px;height:459px}
.welcome-copy{position:absolute;left:645px;top:70px;width:500px}
.welcome-copy h3{font-size:22px;font-weight:700;color:var(--ink);line-height:1.3}
.welcome-copy h2{font-size:30px;font-weight:700;color:var(--ink);margin-bottom:24px;line-height:1.2}
.welcome-copy p{font-size:15px;line-height:1.6;color:#333;margin-bottom:26px}
.welcome-copy .btn{width:132px;height:40px}

/* events */
.event{position:absolute;overflow:hidden;background:radial-gradient(ellipse at 40% 30%,#e2e5e8,#8f979d 55%,#3d4449)}
.event.feature{background:radial-gradient(ellipse at 50% 10%,#f7c47a,#b08f6c 35%,#5a6166 75%,#2e3337)}
.event .date{position:absolute;top:10px;left:0;background:var(--white);font-size:11px;padding:4px 10px;color:#333}
.event .caption{position:absolute;left:18px;right:44px;bottom:16px;color:var(--white)}
.event .caption h4{font-size:17px;font-weight:600;line-height:1.25}
.event.feature .caption h4{font-size:22px}
.event .caption p{font-size:12px;line-height:1.3;opacity:.9}
.event .go{position:absolute;right:12px;bottom:16px;width:26px;height:26px;background:var(--orange);display:flex;align-items:center;justify-content:center}

/* blog */
.blog{top:2527px;left:0;width:1200px;height:657px;background:var(--light)}
.post{position:absolute;top:158px;width:282px;height:434px;background:var(--white);box-shadow:0 2px 8px rgba(0,0,0,.12)}
.post .photo{height:213px}
.post .date{margin:-10px 0 0 30px;position:relative;display:inline-block;background:var(--white);font-size:11px;padding:4px 14px;color:#333}
.post h4{font-size:16px;font-weight:600;color:var(--ink);margin:10px 26px 8px;line-height:1.3}
.post p{font-size:14px;margin:0 26px 18px;line-height:1.4;color:#444}
.post .btn{margin-left:26px;width:100px;height:32px;font-size:11px}

/* gallery */
.tile{position:absolute;width:218px;height:217px}
.gallery-btn{position:absolute;left:519px;top:3833px;width:164px;height:40px}

/* newsletter */
.newsletter{top:3946px;left:0;width:1200px;height:313px;background:radial-gradient(ellipse at 50% 60%,#5a5a5a,#2a2a2a 70%)}
.newsletter h2{position:absolute;top:68px;width:1200px;text-align:center;font-size:30px;font-weight:700;color:var(--white);text-transform:uppercase}
.newsletter p{position:absolute;top:118px;width:1200px;text-align:center;color:#ddd;font-size:16px}
.signup{position:absolute;top:196px;left:318px;width:564px;height:52px;background:var(--white);display:flex;align-items:center;padding:6px}
.signup span{flex:1;padding-left:38px;font-size:14px;color:#555;text-transform:uppercase}
.signup .btn{width:138px;height:40px;font-size:15px}

/* footer */
.site-footer{top:4259px;left:0;width:1200px;height:392px;background:var(--white)}
.footer-brand{position:absolute;left:124px;top:80px;display:flex;align-items:center;gap:12px}
.footer-brand .brand-name{margin-top:-30px}
.footer-col{position:absolute;top:67px;font-size:12px;color:#333}
.footer-col h5{font-size:13px;font-weight:700;color:var(--ink);margin-bottom:18px}
.footer-col li{list-style:none;line-height:1.55;display:flex;gap:12px;align-items:flex-start;margin-bottom:6px}
.menu-col li{margin-bottom:0}
.soc{width:26px;height:26px;border-radius:50%;background:#1d63b8;flex:none}
.rule{position:absolute;left:120px;top:282px;width:960px;height:1px;background:#ddd}
.copyright{position:absolute;top:330px;width:1200px;text-align:center;font-size:12px;color:#444}
.float{position:absolute;top:318px;width:46px;height:46px;border-radius:50%;background:var(--orange);display:flex;align-items:center;justify-content:center}
</style>
</head>
<body>

<header class="site-header abs">
  <div class="brand abs">
    <div class="brand-mark" role="img" aria-label="Kettleworth Supply mascot illustration"></div>
    <div class="brand-name">Kettleworth Supply<small>Used Food Machinery</small></div>
  </div>
  <div class="follow abs">FOLLOW US <span class="dot"></span><span class="dot" style="background:#1da1f2"></span><span class="dot" style="background:#0e76a8"></span></div>
  <div class="call abs">
    <div class="call-icon"><svg width="16" height="16" viewBox="0 0 24 24"><path fill="#fff" d="M6.6 10.8a15.1 15.1 0 0 0 6.6 6.6l2.2-2.2c.3-.3.7-.4 1-.2 1.1.4 2.3.6 3.6.6.6 0 1 .4 1 1V20c0 .6-.4 1-1 1A17 17 0 0 1 3 4c0-.6.4-1 1-1h3.5c.6 0 1 .4 1 1 0 1.2.2 2.4.6 3.6.1.3 0 .7-.2 1z"/></svg></div>
    <div class="call-text">CALL US NOW<b>800.555.0142</b></div>
  </div>
  <ul class="nav abs"><li>HOME</li><li>ABOUT</li><li>SERVICES</li><li>PROJECTS</li><li>BLOG</li><li>CONTACT</li></ul>
</header>

<section class="hero abs" role="img" aria-label="Stainless steel tanks in a food processing plant">
  <h1>FOOD PROCESSING EQUIPMENT</h1>
  <div class="search">
    <div class="field" style="width:217px">Keyword</div>
    <div class="field" style="width:217px">Category <svg width="10" height="6"><path d="M0 0h10L5 6z" fill="#555"/></svg></div>
    <div class="btn">Search</div>
  </div>
  <div class="dots"><i></i><i></i><i></i><i></i><i></i></div>
</section>

<h2 class="section-title" style="top:740px">Past Projects</h2>
<div class="arrow" style="left:0"><svg width="10" height="14"><path d="M8 1L2 7l6 6" stroke="#fff" stroke-width="2" fill="none"/></svg></div>
<div class="arrow" style="left:1168px"><svg width="10" height="14"><path d="M2 1l6 6-6 6" stroke="#fff" stroke-width="2" fill="none"/></svg></div>
<div class="project" style="left:66px"><div class="photo" role="img" aria-label="Used stainless processing machine"></div><div class="project-label">LOREM IPSUM</div></div>
<div class="project" style="left:346px"><div class="photo" role="img" aria-label="Slicing machine"></div><div class="project-label">LOREM IPSUM</div></div>
<div class="project" style="left:626px"><div class="photo" role="img" aria-label="Mixing kettle with control panel"></div><div class="project-label">LOREM IPSUM</div></div>
<div class="project" style="left:906px"><div class="photo" role="img" aria-label="Forming line machine"></div><div class="project-label">LOREM IPSUM</div></div>

<section class="welcome abs">
  <div class="photo" role="img" aria-label="Row of stainless steel storage tanks"></div>
  <div class="welcome-copy">
    <h3>WELCOME TO</h3>
    <h2>KETTLEWORTH SUPPLY</h2>
    <p>Lorem ipsum dolor sit amet, consectetur adipiscing elit, sed do eiusmod tempor incididunt ut labore et dolore magna aliqua. Ut enim ad minim veniam, quis nostrud exercitation ullamco laboris nisi ut aliquip ex ea commodo consequat. Duis aute irure dolor in repreh enderit in voluptate velit esse cillum.</p>
    <div class="btn">Read More</div>
  </div>
</section>

<h2 class="section-title" style="top:1794px">Latest Events</h2>
<article class="event feature" style="left:133px;top:1900px;width:447px;height:543px" role="img" aria-label="Illuminated tank hall">
  <span class="date">Jan 31, 2019</span>
  <div class="caption"><h4>At vero eos et accusamus et iusto odio dignissimos.</h4><p>Voluptatum deleniti atque corrupti quos dolores et quas molestias</p></div>
  <span class="go"><svg width="8" height="10"><path d="M1 1l5 4-5 4" stroke="#fff" stroke-width="2" fill="none"/></svg></span>
</article>
<article class="event" style="left:598px;top:1900px;width:224px;height:264px" role="img" aria-label="Processing tanks">
  <span class="date">Jan 31, 2019</span>
  <div class="caption"><h4>At vero eos et accu</h4><p>Voluptatum deleniti atque corrupti.</p></div>
  <span class="go"><svg width="8" height="10"><path d="M1 1l5 4-5 4" stroke="#fff" stroke-width="2" fill="none"/></svg></span>
</article>
<article class="event" style="left:837px;top:1900px;width:226px;height:264px" role="img" aria-label="Steel vessels">
  <span class="date">Jan 31, 2019</span>
  <div class="caption"><h4>At vero eos et accu</h4><p>Voluptatum deleniti atque corrupti.</p></div>
  <span class="go"><svg width="8" height="10"><path d="M1 1l5 4-5 4" stroke="#fff" stroke-width="2" fill="none"/></svg></span>
</article>
<article class="event" style="left:598px;top:2180px;width:224px;height:263px" role="img" aria-label="Tank room">
  <span class="date">Jan 31, 2019</span>
  <div class="caption"><h4>At vero eos et accu</h4><p>Voluptatum deleniti atque corrupti.</p></div>
  <span class="go"><svg width="8" height="10"><path d="M1 1l5 4-5 4" stroke="#fff" stroke-width="2" fill="none"/></svg></span>
</article>
<article class="event" style="left:837px;top:2180px;width:226px;height:263px;background:radial-gradient(ellipse at 50% 30%,#e9f1f7,#8fb0c6 50%,#3c4d5a)" role="img" aria-label="Filling line">
  <span class="date">Jan 31, 2019</span>
  <div class="caption"><h4>At vero eos et accu</h4><p>Voluptatum deleniti atque corrupti.</p></div>
  <span class="go"><svg width="8" height="10"><path d="M1 1l5 4-5 4" stroke="#fff" stroke-width="2" fill="none"/></svg></span>
</article>

<section class="blog abs">
  <h2 class="section-title" style="top:74px">Latest Blog</h2>
  <article class="post" style="left:146px"><div class="photo" role="img" aria-label="Tank storage hall"></div><span class="date">03 FEB, 2019</span><h4>Lorem Ipsum is simply dum.<br>text of the printing</h4><p>Lorem ipsum dolor sit amet, consectetur adipiscing elit, sed do eiusmod tempo.</p><div class="btn">Read More</div></article>
  <article class="post" style="left:459px"><div class="photo" role="img" aria-label="Baked goods on a production conveyor" style="background:radial-gradient(ellipse at 50% 60%,#e3b878,#9a8a74 50%,#4c4944)"></div><span class="date">03 FEB, 2019</span><h4>Lorem Ipsum is simply dum.<br>text of the printing</h4><p>Lorem ipsum dolor sit amet, consectetur adipiscing elit, sed do eiusmod tempo.</p><div class="btn">Read More</div></article>
  <article class="post" style="left:775px"><div class="photo" role="img" aria-label="Blue-lit steel vessels" style="background:radial-gradient(ellipse at 40% 40%,#d6e2ee,#7f95ab 50%,#2f3e4c)"></div><span class="date">03 FEB, 2019</span><h4>Lorem Ipsum is simply dum.<br>text of the printing</h4><p>Lorem ipsum dolor sit amet, consectetur adipiscing elit, sed do eiusmod tempo.</p><div class="btn">Read More</div></article>
</section>

<h2 class="section-title" style="top:3247px">Gallery</h2>
<div class="tile photo" style="left:146px;top:3348px" role="img" aria-label="Tank room"></div>
<div class="tile photo" style="left:376px;top:3348px;background:radial-gradient(ellipse at 40% 40%,#c9d5e1,#6f8296 55%,#2e3b48)" role="img" aria-label="Steel tanks"></div>
<div class="tile photo" style="left:606px;top:3348px;background:radial-gradient(ellipse at 60% 30%,#f0f2f4,#a5adb4 55%,#5c646b)" role="img" aria-label="Tank close-up"></div>
<div class="tile photo" style="left:837px;top:3348px;background:radial-gradient(ellipse at 70% 15%,#f4a35c,#8e7a6a 45%,#3e4347)" role="img" aria-label="Lit production hall"></div>
<div class="tile photo" style="left:146px;top:3578px;background:radial-gradient(ellipse at 30% 30%,#ecd9b6,#a7a49c 50%,#5e656b)" role="img" aria-label="Mixing bowl"></div>
<div class="tile photo" style="left:376px;top:3578px;background:radial-gradient(ellipse at 50% 50%,#bcc8d3,#67788a 55%,#2c3540)" role="img" aria-label="Tank interior"></div>
<div class="tile photo" style="left:606px;top:3578px;background:radial-gradient(ellipse at 50% 40%,#e5edf4,#8aa8c2 55%,#45596c)" role="img" aria-label="Pipework"></div>
<div class="tile photo" style="left:837px;top:3578px;background:radial-gradient(ellipse at 55% 50%,#e1e4e7,#8d959c 55%,#3f464c)" role="img" aria-label="Vessel hatch"></div>
<div class="btn gallery-btn">View All Images</div>

<section class="newsletter abs" role="img" aria-label="Dark tank hall backdrop">
  <h2>Newsletter Subscribe</h2>
  <p>Lorem ipsum dolor sit amet consectetur</p>
  <div class="signup">
    <svg style="position:absolute;left:22px" width="16" height="12"><rect x=".5" y=".5" width="15" height="11" fill="none" stroke="#555"/><path d="M1 1l7 5 7-5" stroke="#555" fill="none"/></svg>
    <span>E-mail ID</span><div class="btn">Subscribe</div>
  </div>
</section>

<footer class="site-footer abs">
  <div class="footer-brand">
    <div class="brand-mark" role="img" aria-label="Kettleworth Supply mascot illustration"></div>
    <div class="brand-name">Kettleworth Supply<small>Used Food Machinery</small></div>
  </div>
  <div class="footer-col" style="left:567px">
    <h5>CONTACT US</h5>
    <ul>
      <li><svg width="10" height="14"><path d="M5 0a5 5 0 0 1 5 5c0 4-5 9-5 9S0 9 0 5a5 5 0 0 1 5-5z" fill="#333"/></svg><span>12 Foundry Lane<br>Millbrook, IL 60400</span></li>
      <li><svg width="12" height="12" viewBox="0 0 24 24"><path fill="#333" d="M6.6 10.8a15.1 15.1 0 0 0 6.6 6.6l2.2-2.2c.3-.3.7-.4 1-.2 1.1.4 2.3.6 3.6.6.6 0 1 .4 1 1V20c0 .6-.4 1-1 1A17 17 0 0 1 3 4c0-.6.4-1 1-1h3.5c.6 0 1 .4 1 1 0 1.2.2 2.4.6 3.6.1.3 0 .7-.2 1z"/></svg><span>800-555-0142</span></li>
      <li><svg width="12" height="10"><rect x=".5" y=".5" width="11" height="9" fill="none" stroke="#333"/><path d="M1 1l5 4 5-4" stroke="#333" fill="none"/></svg><span>hello@kettleworth.example</span></li>
    </ul>
  </div>
  <div class="footer-col menu-col" style="left:815px">
    <h5>MENU</h5>
    <ul><li>HOME</li><li>ABOUT</li><li>SERVICES</li><li>PROJECTS</li><li>BLOG</li><li>CONTACT</li></ul>
  </div>
  <div class="footer-col" style="left:940px">
    <h5>CONNECT WITH US</h5>
    <ul>
      <li style="align-items:center"><span class="soc"></span>Social One</li>
      <li style="align-items:center"><span class="soc" style="background:#1da1f2"></span>Social Two</li>
      <li style="align-items:center"><span class="soc" style="background:#0e76a8"></span>Social Three</li>
    </ul>
  </div>
  <div class="rule"></div>
  <p class="copyright">Copyright © 2019 All Rights Reserved</p>
  <div class="float" style="left:968px"><svg width="18" height="18"><circle cx="7.5" cy="7.5" r="5.5" stroke="#fff" stroke-width="2" fill="none"/><path d="M11.5 11.5l5 5" stroke="#fff" stroke-width="2"/></svg></div>
  <div class="float" style="left:1023px"><svg width="16" height="16" viewBox="0 0 24 24"><path fill="#fff" d="M6.6 10.8a15.1 15.1 0 0 0 6.6 6.6l2.2-2.2c.3-.3.7-.4 1-.2 1.1.4 2.3.6 3.6.6.6 0 1 .4 1 1V20c0 .6-.4 1-1 1A17 17 0 0 1 3 4c0-.6.4-1 1-1h3.5c.6 0 1 .4 1 1 0 1.2.2 2.4.6 3.6.1.3 0 .7-.2 1z"/></svg></div>
</footer>

</body>
</html>
```